Modern card design needed for building development company

We are looking for a sharp modern new look for our business cards.
We are a New Zealand based company called TKV Ventures NZ LTD that specialises in subdividing large sections, housing and commercial buildings.
We have attached a photo of the current logo and would like to see it improved somehow as it looks a bit dated.
We are open to any colours.

Target Market(s)

Investors, Property buyers

Industry/Entity Type

Investment

Contact Information for Business Card

TKV VENTURES NZ LTD
www.tkvventuresnz.co.nz

Howard Pennick
Phone +64 21 843 192
Email hdpennick@fernmail.co.nz

Font styles to use
Serif
Sans Serif

Colors
0792cd
33a6d7
85cae6
6b449b
886aae
f04a50
ec1f27
f37122
f68d4d

Requirements
Must have
• Please try and make the logo more modern or if you have a similar one we would like to see it.

```html
<!DOCTYPE html>
<html lang="en">
<head>
<meta charset="utf-8">
<title>TKV Ventures NZ LTD – Business Card</title>
<link rel="stylesheet" href="https://fonts.googleapis.com/css2?family=Montserrat:wght@400;500;600;700&display=swap">
<style>
  :root {
    --backdrop: #2a2a2a;
    --card: #f4f4f2;
    --brand-blue: #1a6fc4;
    --ink: #141414;
    --ink-soft: #333333;
  }
  * { box-sizing: border-box; margin: 0; padding: 0; }
  html, body {
    width: 1200px;
    height: 1000px;
    overflow: hidden;
  }
  body {
    background: var(--backdrop);
    font-family: "Montserrat", Arial, sans-serif;
    position: relative;
  }
  .card {
    position: absolute;
    left: 270px;
    width: 660px;
    height: 377px;
    background: var(--card);
    box-shadow: 0 10px 30px rgba(0,0,0,0.45);
  }
  .card--front { top: 90px; }
  .card--back { top: 520px; }

  .wordmark {
    color: var(--ink);
    font-weight: 600;
    line-height: 1;
    white-space: nowrap;
  }

  .card--front .wordmark {
    position: absolute;
    top: 140px;
    left: 0;
    right: 0;
    text-align: center;
    font-size: 68px;
  }
  .front__web {
    position: absolute;
    bottom: 58px;
    left: 0;
    right: 0;
    text-align: center;
    font-size: 17px;
    font-weight: 700;
    color: var(--ink);
  }
  .web__domain { color: var(--brand-blue); }

  .card--back .wordmark {
    position: absolute;
    left: 58px;
    top: 166px;
    font-size: 42px;
  }
  .back__divider {
    position: absolute;
    left: 326px;
    top: 112px;
    width: 3px;
    height: 150px;
    background: var(--brand-blue);
  }
  .contact {
    position: absolute;
    left: 350px;
    top: 112px;
    list-style: none;
  }
  .contact__name {
    font-size: 20px;
    font-weight: 700;
    color: var(--brand-blue);
    margin-bottom: 10px;
  }
  .contact__company {
    font-size: 15px;
    font-weight: 700;
    color: var(--ink);
    margin-bottom: 8px;
  }
  .contact__row {
    display: flex;
    align-items: center;
    gap: 8px;
    font-size: 15px;
    font-weight: 500;
    color: var(--ink-soft);
    margin-bottom: 5px;
    white-space: nowrap;
  }
  .contact__icon { width: 14px; height: 14px; flex: none; }
  .contact__row .web__domain { font-weight: 600; }
</style>
</head>
<body>
  <section class="card card--front">
    <div class="wordmark">Trueward</div>
    <p class="front__web">www.<span class="web__domain">tkvventuresnz</span>.co.nz</p>
  </section>

  <section class="card card--back">
    <div class="wordmark">Trueward</div>
    <div class="back__divider"></div>
    <ul class="contact">
      <li class="contact__name">Howard Pennick</li>
      <li class="contact__company">TKV VENTURES NZ LTD</li>
      <li class="contact__row">
        <svg class="contact__icon" viewBox="0 0 16 16" aria-hidden="true">
          <circle cx="8" cy="8" r="8" fill="#1a6fc4"/>
          <path d="M5.2 4.2l1.4-.3.8 2-1 .8c.5 1.1 1.3 1.9 2.4 2.4l.8-1 2 .8-.3 1.4c-3.6.3-6.4-2.5-6.1-6.1z" fill="#fff"/>
        </svg>
        <span>+64 21 843 192</span>
      </li>
      <li class="contact__row">
        <svg class="contact__icon" viewBox="0 0 16 16" aria-hidden="true">
          <rect x="1" y="3" width="14" height="10" rx="1" fill="none" stroke="#1a6fc4" stroke-width="1.5"/>
          <path d="M1.5 3.8L8 9l6.5-5.2" fill="none" stroke="#1a6fc4" stroke-width="1.5"/>
        </svg>
        <span>hdpennick@fernmail.co.nz</span>
      </li>
      <li class="contact__row">
        <svg class="contact__icon" viewBox="0 0 16 16" aria-hidden="true">
          <circle cx="8" cy="8" r="6.8" fill="none" stroke="#1a6fc4" stroke-width="1.4"/>
          <ellipse cx="8" cy="8" rx="3" ry="6.8" fill="none" stroke="#1a6fc4" stroke-width="1.2"/>
          <path d="M1.2 8h13.6M2.3 4.6h11.4M2.3 11.4h11.4" stroke="#1a6fc4" stroke-width="1.1"/>
        </svg>
        <span>www.<span class="web__domain">tkvventuresnz</span>.co.nz</span>
      </li>
    </ul>
  </section>
</body>
</html>
```